electrical contractor business card for professional modern company

I need a business card design for an electrical contractors business. I do all kinds of electricical work from new homes, air conditioning, data and communications. I have a logo design i want on it and have a good idea in my head of what i want it to look like. I like simple yet bold and professional looking. All black background is a must

Target Market(s)

Anyone needing electrical work done

Industry/Entity Type

Electrical

Contact Information for Business Card

company name- KTW Electrical and Data
person name-martin pellowe
phone number- 0418 362 927
website-ktwelec.example.com.au

Font styles to use
Sans Serif

Requirements
Must have
• email
• website
• logo
• name
• phone number
• list of work i do:
• -electrical
• -air-conditioning
• -data/communications
• -cctv/security
• -domestic/commercial/industrial
• -24hr emergency breakdown repair
Nice to have
• i would like the logo on the front side in the centre taking up most of the card with black background.
• on the rear i want the list of work i do with company info i.e. email, website, my name, phone number. rear of card also black background with orange writing to match the orange in the logo

```html
<!DOCTYPE html>
<html lang="en">
<head>
<meta charset="utf-8">
<title>KTW Electrical and Data – Business Card</title>
<link rel="stylesheet" href="https://fonts.googleapis.com/css2?family=Open+Sans:wght@400;600;700&display=swap">
<style>
  :root {
    --backdrop: #9b9b9b;
    --card: #111111;
    --ink: #f2f2f2;
    --orange: #f26a1b;
    --muted: #9a9a9a;
  }
  * { margin: 0; padding: 0; box-sizing: border-box; }
  html, body {
    width: 1200px; height: 720px; overflow: hidden;
    background: var(--backdrop);
    font-family: "Open Sans", Arial, sans-serif;
    color: var(--ink);
  }
  .stage {
    width: 1200px; height: 720px;
    display: flex; align-items: center; justify-content: center; gap: 40px;
  }
  .card {
    width: 540px; height: 330px;
    background: var(--card);
    position: relative;
    box-shadow: 0 6px 18px rgba(0,0,0,.3);
    overflow: hidden;
  }
  /* front */
  .card--front {
    display: flex; flex-direction: column; align-items: center; justify-content: center; gap: 44px;
  }
  .brand {
    display: flex; align-items: center; gap: 12px;
    color: var(--orange); font-weight: 700; white-space: nowrap;
  }
  .brand__dot { width: 16px; height: 16px; border-radius: 50%; background: var(--orange); flex: none; }
  .card--front .brand { font-size: 30px; }
  .tagline {
    font-size: 16px; letter-spacing: 4px; text-transform: uppercase;
    color: var(--ink); white-space: nowrap;
  }
  /* back */
  .card--back .brand { position: absolute; left: 40px; top: 40px; font-size: 22px; }
  .holder { position: absolute; left: 40px; top: 98px; }
  .holder__name { color: var(--orange); font-weight: 700; font-size: 19px; }
  .holder__role { color: var(--muted); font-size: 13px; }
  .contacts {
    position: absolute; left: 40px; top: 176px;
    list-style: none; font-size: 13.5px; line-height: 24px; white-space: nowrap;
  }
  .contacts li { display: flex; align-items: center; gap: 10px; }
  .contacts svg { width: 14px; height: 14px; fill: var(--orange); flex: none; }
  .services {
    position: absolute; left: 292px; bottom: 28px;
    list-style: none; font-size: 14px; line-height: 23px; white-space: nowrap;
  }
  .services li { display: flex; align-items: center; gap: 9px; }
  .services svg { width: 11px; height: 11px; fill: var(--orange); flex: none; }
</style>
</head>
<body>
<main class="stage">
  <section class="card card--front">
    <div class="brand"><span class="brand__dot"></span>KTW Electrical and Data</div>
    <p class="tagline">24 Hour Emergency Breakdown Repair</p>
  </section>

  <section class="card card--back">
    <div class="brand"><span class="brand__dot"></span>KTW Electrical and Data</div>
    <div class="holder">
      <p class="holder__name">Martin Pellowe</p>
      <p class="holder__role">Chief Executive</p>
    </div>
    <ul class="contacts">
      <li><svg viewBox="0 0 24 24"><path d="M6.6 10.8a15 15 0 0 0 6.6 6.6l2.2-2.2a1 1 0 0 1 1-.25 11.4 11.4 0 0 0 3.6.57 1 1 0 0 1 1 1V20a1 1 0 0 1-1 1A17 17 0 0 1 3 4a1 1 0 0 1 1-1h3.5a1 1 0 0 1 1 1c0 1.25.2 2.45.57 3.57a1 1 0 0 1-.25 1z"/></svg>0418 362 927</li>
      <li><svg viewBox="0 0 24 24"><path d="M2 5h20v14H2zm2 2v.5l8 5 8-5V7zm0 2.9V17h16V9.9l-8 5z"/></svg>info@ktwelec.example.com.au</li>
      <li><svg viewBox="0 0 24 24"><path d="M12 2a10 10 0 1 0 0 20 10 10 0 0 0 0-20zm6.9 6h-3a15 15 0 0 0-1.3-3.8A8 8 0 0 1 18.9 8zM12 4c.9 1.2 1.6 2.6 2 4h-4c.4-1.4 1.1-2.8 2-4zM4.3 14a8 8 0 0 1 0-4h3.4a16 16 0 0 0 0 4zm.8 2h3a15 15 0 0 0 1.3 3.8A8 8 0 0 1 5.1 16zm3-8h-3a8 8 0 0 1 4.3-3.8A15 15 0 0 0 8.1 8zM12 20c-.9-1.2-1.6-2.6-2-4h4c-.4 1.4-1.1 2.8-2 4zm2.3-6H9.7a14 14 0 0 1 0-4h4.6a14 14 0 0 1 0 4zm.3 5.8a15 15 0 0 0 1.3-3.8h3a8 8 0 0 1-4.3 3.8zm1.7-5.8a16 16 0 0 0 0-4h3.4a8 8 0 0 1 0 4z"/></svg>www.ktwelec.example.com.au</li>
    </ul>
    <ul class="services">
      <li><svg viewBox="0 0 24 24"><path d="M12 2l3 7h7l-5.5 4.5 2 7.5-6.5-4.5-6.5 4.5 2-7.5L2 9h7z"/></svg>Electrical</li>
      <li><svg viewBox="0 0 24 24"><path d="M12 2l3 7h7l-5.5 4.5 2 7.5-6.5-4.5-6.5 4.5 2-7.5L2 9h7z"/></svg>Cctv, security</li>
      <li><svg viewBox="0 0 24 24"><path d="M12 2l3 7h7l-5.5 4.5 2 7.5-6.5-4.5-6.5 4.5 2-7.5L2 9h7z"/></svg>Air-conditioning</li>
      <li><svg viewBox="0 0 24 24"><path d="M12 2l3 7h7l-5.5 4.5 2 7.5-6.5-4.5-6.5 4.5 2-7.5L2 9h7z"/></svg>Data, communication</li>
      <li><svg viewBox="0 0 24 24"><path d="M12 2l3 7h7l-5.5 4.5 2 7.5-6.5-4.5-6.5 4.5 2-7.5L2 9h7z"/></svg>Domestic, commercial, industrial</li>
    </ul>
  </section>
</main>
</body>
</html>
```